Tales from Kin Logo Design plus business cards design

We are a start up company that will help seniors write their memoirs...beginning with a few ancestors and their heritage and continuing through their own history...how they would like to be remembered in the next generation. I envision a card with a senior citizen at an older writing desk, writing her memoirs, with a book (maybe standing on top, leaning slightly) that has the words Tales from Kin.com on the back binding. OR maybe a senior couple walking into the sunset with the same book somewhere in the frame. Communicating the relevance of every life being significant to those that come after them...when a genealogy doesn't say enough about the details of ones life. Please note that I am open to the professionals own ideas...I am not locked into my concepts. On the back of the card I would like one or two phrases..."A Genealogy Doesn't Say Enough" and/or "Every life legacy is uniquely significant to the next generation".
Updates

I have added a couple of photos for ideas that may be used if needed.

I have both increased and committed the payment! Thanks for the reminder!

Reason: We increased the payment commitment and added some photo ideas to help.

We want to thank EVERYONE who participated in this contest. There were so many wonderful and VERY professional proposals...making it very challenging to decide on one! We are posting a new contest for a brochure now and hope many of you will participate. May God bless your endeavors.

Target Market(s)

Senior populous & baby boomer generation.

Industry/Entity Type

Business

Logo Text

Tales from Kin ordinary lives...extraordinary legacy

Requirements
Must have
• Relevant info:
Domain name: talesfromkin.com
email: info@talesfromkin.com
phone: 1-855-GAB-TALE toll free
1-717-382-5619 local
name: Doris Whitlock, M.A.
Nice to have
• photo of senior or senior couple....book with our web address on the binding. I attached two photos that could work if cropped and enhanced. Words need to be deleted from the one photo of senior at a writing desk and couple on the beach could use a sunset sky and other people cropped out. Just ideas...don't know if you have better ones or prefer a different idea.

```html
<!DOCTYPE html>
<html lang="en">
<head>
<meta charset="utf-8">
<title>Tales from Kin – Business Card</title>
<link rel="stylesheet" href="https://fonts.googleapis.com/css2?family=Cousine:wght@400;700&display=swap">
<style>
  :root {
    --sky-deep: #00a9e6;
    --sky-mid: #4cc3ee;
    --sky-pale: #cfeefa;
    --paper: #fffefa;
    --ink: #1c1c1c;
    --sea-teal: #1fa9a3;
    --coat-slate: #3a5866;
    --coat-red: #e0243a;
  }
  html, body {
    margin: 0;
    padding: 0;
    width: 1200px;
    height: 686px;
    overflow: hidden;
    background: var(--paper);
  }
  .card {
    position: relative;
    width: 1200px;
    height: 686px;
    overflow: hidden;
    background: var(--paper);
    font-family: "Cousine", monospace;
    color: var(--ink);
  }
  .sky-wash {
    position: absolute;
    inset: 0 0 auto 0;
    height: 440px;
    background: linear-gradient(180deg,
      var(--sky-deep) 0%,
      var(--sky-deep) 14%,
      var(--sky-mid) 34%,
      var(--sky-pale) 56%,
      var(--paper) 100%);
  }
  .brand-name {
    position: absolute;
    left: 103px;
    top: 212px;
    margin: 0;
    font-size: 104px;
    font-weight: 400;
    letter-spacing: 8px;
    line-height: 1;
    color: var(--ink);
    white-space: nowrap;
  }
  .couple-scene {
    position: absolute;
    left: 756px;
    top: 366px;
    width: 444px;
    height: 320px;
    background: linear-gradient(90deg,
      rgba(255,254,250,0) 0%,
      var(--sea-teal) 22%,
      var(--coat-slate) 50%,
      var(--coat-red) 72%,
      var(--sea-teal) 88%,
      rgba(255,254,250,0) 100%);
    opacity: 0.85;
  }
  .contact {
    position: absolute;
    left: 91px;
    top: 400px;
    margin: 0;
  }
  .contact__name {
    font-size: 32px;
    font-weight: 700;
    letter-spacing: 1px;
    margin: 0 0 8px;
    line-height: 44px;
  }
  .contact__line {
    font-size: 32px;
    font-weight: 400;
    line-height: 40px;
    margin: 0;
    white-space: nowrap;
  }
</style>
</head>
<body>
  <div class="card">
    <div class="sky-wash" role="img" aria-label="Watercolour wash of blue sky fading into white"></div>

    <h1 class="brand-name">Tales from Kin</h1>

    <div class="couple-scene" role="img" aria-label="Painted senior couple walking along a teal shoreline, seen from behind"></div>

    <address class="contact">
      <p class="contact__name">DORIS WHITLOCK, M.A.,</p>
      <p class="contact__line">1-855-GAB-TALE toll free</p>
      <p class="contact__line">1-717-382-5619 local</p>
      <p class="contact__line">info@talesfromkin.com</p>
      <p class="contact__line">www.talesfromkin.com</p>
    </address>
  </div>
</body>
</html>
```